Graphic Design for Beauty Blister Packaging

Seeking visionary designers to create next-level packaging concepts for a dermaplaning tool targeted at North American women aged 18-65. This project combines innovation, elegance, and modern trends, with a particular focus on Y2K-inspired aesthetics blended with minimalist luxury.

See below and attached word document for guidelines and image of product.

What We're Looking For:
We want packaging that not only turns heads but also tells a story of sophistication and self-care. Your design should communicate the following key elements:

Premium Look: Incorporate holographic or foil stamping elements for a high-end, futuristic feel.
Functionality Meets Elegance: Design a clean, user-friendly layout that highlights product benefits and ensures clarity for the customer.
Visual Appeal: Capture a balance between Y2K retro vibes (think holographics, gradients, bold fonts) and modern minimalism (clean lines, simple typography, and elegant spacing).
Brand Integration: Seamlessly incorporate the Movrenta logo and branding elements into your design.
Design Objectives:

Stand out on shelves with a unique, innovative look.
Appeal to a wide demographic by combining timeless beauty with trendy appeal.
Highlight product features such as “Exfoliates,” “Shapes Eyebrows,” and “Removes Fine Hairs” in a way that is both enticing and informative.

Submission Guidelines:

Use holographic gradients and foil stamping as key features of your design.
Include a window to display the product while incorporating chrome-like or holographic borders.
Ensure typography is bold, clean, and aligns with the Y2K theme while being highly legible.
Add a mock-up of how your design would look in retail displays.

Target Market(s)

Women aged 18-65

Industry/Entity Type

Beauty and Cosmetics

Font styles to use
Sans Serif

Requirements
Nice to have
• Y2k theme in a minimalistic style
Should not have
• Cluttered design, excessive icons or designs

```html
<!DOCTYPE html>
<html lang="en">
<head>
<meta charset="utf-8">
<title>Movrenta Dermaplaning Tool – Blister Card</title>
<link rel="stylesheet" href="https://fonts.googleapis.com/css2?family=Poppins:wght@400;500;600;700;800&display=swap">
<style>
  :root {
    --page: #ffffff;
    --deep-purple: #5e0b7c;
    --magenta: #e21fd4;
    --band-top: #9620c8;
    --band-bottom: #3f0a52;
    --window-line: #e8322f;
    --ink: #141414;
    --white: #ffffff;
    --holo-lilac: #c7cdeb;
    --holo-pink: #eeb3dc;
    --holo-mint: #b5f4d2;
    --holo-violet: #d9b2ee;
  }
  html, body {
    margin: 0;
    padding: 0;
    width: 1013px;
    height: 1200px;
    overflow: hidden;
    background: var(--page);
  }
  .blister-card {
    display: block;
    width: 1013px;
    height: 1200px;
    font-family: "Poppins", sans-serif;
  }
  .title { font-weight: 800; font-size: 39px; fill: var(--deep-purple); letter-spacing: -0.5px; }
  .subtitle { font-weight: 400; font-size: 22px; fill: var(--magenta); }
  .pack-label { font-weight: 600; font-size: 22px; fill: var(--white); }
  .benefit { font-weight: 600; font-size: 17.5px; fill: var(--white); }
  .badge-text { font-weight: 500; font-size: 10px; fill: var(--white); letter-spacing: 1px; }
  .brand-name { font-weight: 400; font-size: 34px; fill: var(--ink); letter-spacing: -0.5px; }
  .origin-small { font-weight: 600; font-size: 12.5px; fill: var(--ink); letter-spacing: 1.6px; }
  .origin-large { font-weight: 800; font-size: 26px; fill: var(--ink); letter-spacing: 1px; }
  .tagline { font-weight: 500; font-size: 14.5px; fill: var(--deep-purple); }
</style>
</head>
<body>
<svg class="blister-card" viewBox="0 0 1013 1200" xmlns="http://www.w3.org/2000/svg">
  <defs>
    <linearGradient id="holo-card" x1="0" y1="0" x2="1" y2="1">
      <stop offset="0" stop-color="var(--holo-lilac)"/>
      <stop offset="0.2" stop-color="var(--holo-mint)"/>
      <stop offset="0.38" stop-color="var(--holo-pink)"/>
      <stop offset="0.55" stop-color="var(--holo-lilac)"/>
      <stop offset="0.72" stop-color="var(--holo-violet)"/>
      <stop offset="0.86" stop-color="var(--holo-mint)"/>
      <stop offset="1" stop-color="var(--holo-lilac)"/>
    </linearGradient>
    <linearGradient id="holo-window" x1="0" y1="0" x2="1" y2="0.6">
      <stop offset="0" stop-color="var(--holo-pink)"/>
      <stop offset="0.35" stop-color="var(--holo-mint)"/>
      <stop offset="0.65" stop-color="var(--holo-lilac)"/>
      <stop offset="1" stop-color="var(--holo-violet)"/>
    </linearGradient>
    <linearGradient id="purple-band" x1="0" y1="0" x2="0" y2="1">
      <stop offset="0" stop-color="var(--band-top)"/>
      <stop offset="1" stop-color="var(--band-bottom)"/>
    </linearGradient>
    <linearGradient id="steel" x1="0" y1="0" x2="1" y2="1">
      <stop offset="0" stop-color="#f2f2f2"/>
      <stop offset="0.5" stop-color="#9a9a9a"/>
      <stop offset="1" stop-color="#e6e6e6"/>
    </linearGradient>
    <path id="badge-arc" d="M 532 752 A 44 44 0 1 1 612 750"/>
  </defs>

  <!-- Card body -->
  <rect class="card-body" x="263" y="234" width="489" height="735" rx="36" fill="url(#holo-card)"/>

  <!-- Hang hole -->
  <path class="hang-hole" d="M 459 278 L 496 278 Q 496 266 508 266 Q 520 266 520 278 L 557 278 A 12.5 12.5 0 0 1 557 303 L 459 303 A 12.5 12.5 0 0 1 459 278 Z"
        fill="var(--white)" stroke="var(--ink)" stroke-width="1.2"/>

  <!-- Headings -->
  <text class="title" x="508" y="359" text-anchor="middle">DERMAPLANING TOOL</text>
  <text class="subtitle" x="508" y="389" text-anchor="middle">FOLDABLE COMPACT RAZORS</text>

  <!-- Blister seal guide -->
  <path class="seal-guide" d="M 340 380 Q 300 388 288 430 L 340 860 Q 345 884 370 884 L 640 884 Q 672 884 678 850 L 680 648 Q 690 632 708 620 Q 722 520 728 430 Q 724 390 680 380"
        fill="none" stroke="#8f8f9a" stroke-width="0.8" stroke-dasharray="7 6"/>

  <!-- Product window -->
  <path class="product-window" d="M 338 411 L 677 411 Q 696 411 695 432 Q 688 530 675 588 Q 670 600 660 612 Q 651 622 650 640 L 643 833 Q 642 852 622 852 L 388 852 Q 373 852 370 836 L 321 443 Q 319 411 338 411 Z"
        fill="url(#holo-window)" stroke="var(--window-line)" stroke-width="1.2"/>

  <!-- Product info band -->
  <path class="info-band" d="M 348 618 Q 400 612 470 630 Q 560 656 638 652 L 633 832 Q 632 842 622 842 L 390 842 Q 381 842 379 832 Z"
        fill="url(#purple-band)"/>

  <text class="pack-label" x="389" y="682">9 PACK</text>
  <text class="pack-label" x="389" y="705">FOLDABLE</text>
  <text class="pack-label" x="389" y="728">RAZORS</text>

  <!-- Benefits -->
  <g class="benefit-list">
    <g transform="translate(402 758)">
      <circle r="6.5" fill="none" stroke="var(--magenta)" stroke-width="1.3"/>
      <path d="M -3 0 L -0.7 2.6 L 3.5 -3" fill="none" stroke="var(--magenta)" stroke-width="1.5"/>
    </g>
    <text class="benefit" x="414" y="764">Exfoliates</text>
    <g transform="translate(402 781)">
      <circle r="6.5" fill="none" stroke="var(--magenta)" stroke-width="1.3"/>
      <path d="M -3 0 L -0.7 2.6 L 3.5 -3" fill="none" stroke="var(--magenta)" stroke-width="1.5"/>
    </g>
    <text class="benefit" x="414" y="787">Shapes Eyebrow</text>
    <g transform="translate(402 804)">
      <circle r="6.5" fill="none" stroke="var(--magenta)" stroke-width="1.3"/>
      <path d="M -3 0 L -0.7 2.6 L 3.5 -3" fill="none" stroke="var(--magenta)" stroke-width="1.5"/>
    </g>
    <text class="benefit" x="414" y="810">Removes Fine Hairs</text>
  </g>

  <!-- Steel badge -->
  <g class="steel-badge">
    <circle cx="570" cy="727" r="35" fill="url(#steel)" stroke="var(--white)" stroke-width="1.5"
            role="img" aria-label="Close-up photo of the stainless steel razor blade edge"/>
    <text class="badge-text"><textPath href="#badge-arc" startOffset="50%" text-anchor="middle">SWEDISH STAINLESS STEEL</textPath></text>
  </g>

  <!-- Brand -->
  <text class="brand-name" x="340" y="914">Movrenta</text>

  <!-- Origin mark -->
  <g class="origin-flag" role="img" aria-label="US flag">
    <rect x="587" y="893" width="55" height="34" fill="var(--ink)"/>
    <rect x="587" y="897" width="55" height="2.5" fill="var(--holo-lilac)"/>
    <rect x="612" y="903" width="30" height="2.5" fill="var(--holo-lilac)"/>
    <rect x="612" y="909" width="30" height="2.5" fill="var(--holo-lilac)"/>
    <rect x="587" y="915" width="55" height="2.5" fill="var(--holo-lilac)"/>
    <rect x="587" y="921" width="55" height="2.5" fill="var(--holo-lilac)"/>
  </g>
  <text class="origin-small" x="646" y="904">MADE IN</text>
  <text class="origin-large" x="645" y="927">USA</text>

  <text class="tagline" x="507" y="956" text-anchor="middle">SIMPLY INNOVATIVE SKIN CARE</text>
</svg>
</body>
</html>
```